Need Cool Athletic Ticket Design for Students to use to enter a High School Athletic Sports Contest

I am needing a Event Ticket design for the Brenwick High School Athletics department (https://bhs.brenwickps.com/). This will be a general admission ticket for ALL SPORTS. It will not be sport specific. The ticket will be 5.5" X 2" with serial numbering and perforation. It will also be a front and back ticket with the Brenwick Athletics ticket design on one side and a Harvestline Insurance Sponsorship ad design on the back. I have attached some ticket examples. The right side of the perforation must include space for the customer to fill out name, address, phone and email. It must include the ticket serial number on both portions, on the front side, of the ticket.

Requirements
Must have
• 5.5" X 2" ticket must have serial numbering and perforation. It must contain General Admission Ticket on the Brenwick HS Side and a Harvestline Ad (Doran Pike Agency) on the back side of the ticket.
• The Harvestline side of the Ticket will look similar to the business card (attached file) but please REMOVE the Direct phone (555-214-6730) and the email address (dpike@harvestlineagent.example). In place of the email address please add the agency's web address: www.harvestlineagent.example/dpike
• TAG LINE (at the bottom of the Harvestline AD): Take the DORAN PIKE CHALLENGE: If I can't save you money on your Auto Insurance; I'll buy you Dinner!
Nice to have
• Cool background graphics with the Brenwick HS Logo on the top of the background.
Should not have
• Must NOT be sport specific.

```html
<!DOCTYPE html>
<html lang="en">
<head>
<meta charset="utf-8">
<title>Brenwick High School Admission Ticket</title>
<link rel="stylesheet" href="https://fonts.googleapis.com/css2?family=Alfa+Slab+One&family=Graduate&family=Libre+Baskerville:wght@700&family=Roboto+Condensed:wght@400;700&display=swap">
<style>
  :root {
    --page: #e4e5e7;
    --ink-dark: #1f2021;
    --ink-mid: #34383a;
    --red: #e8141f;
    --white: #ffffff;
    --rule: #8a8a8a;
    --photo-warm: #7a6058;
    --photo-cool: #3d3a44;
    --label: #111111;
    --pill-text: #9a9a9a;
  }
  * { margin: 0; padding: 0; box-sizing: border-box; }
  html, body { width: 1200px; height: 1200px; overflow: hidden; background: var(--page); }
  .canvas { position: relative; width: 1200px; height: 1200px; }

  .ticket { position: absolute; overflow: hidden; }
  .ticket--front { left: 89px; top: 124px; width: 955px; height: 347px; }
  .ticket--back { left: 118px; top: 544px; width: 948px; height: 344px; background: linear-gradient(135deg, #2a2b2c, #161717); }

  .sports-backdrop { position: absolute; inset: 0; background: radial-gradient(ellipse at 50% 40%, var(--ink-mid), var(--ink-dark) 75%); }
  .red-band { position: absolute; left: 0; top: 0; width: 110px; height: 347px; }

  .school-mark { position: absolute; display: flex; align-items: center; font-family: "Graduate", serif; color: var(--red); white-space: nowrap; }
  .school-mark__box { background: var(--red); }
  .school-mark--main { left: 138px; top: 52px; font-size: 22px; gap: 6px; }
  .school-mark--main .school-mark__box { width: 13px; height: 13px; }
  .school-mark--stub { left: 680px; top: 61px; font-size: 12px; gap: 4px; }
  .school-mark--stub .school-mark__box { width: 9px; height: 9px; }

  .serial { position: absolute; background: var(--white); border-radius: 20px; font-family: "Roboto Condensed", sans-serif; font-weight: 700; color: var(--pill-text); display: flex; align-items: center; }
  .serial--main { left: 372px; top: 53px; width: 202px; height: 31px; padding-left: 12px; font-size: 12px; }
  .serial--stub { left: 794px; top: 58px; width: 152px; height: 23px; padding-left: 10px; font-size: 11px; }

  .school-name { position: absolute; left: 183px; top: 134px; font-family: "Alfa Slab One", serif; font-weight: 400; color: var(--white); -webkit-text-stroke: 1.5px #000; paint-order: stroke fill; line-height: 1; white-space: nowrap; }
  .school-name__line { display: block; font-size: 54px; letter-spacing: 1px; }
  .school-name__line + .school-name__line { margin-top: 14px; }

  .admission { position: absolute; left: 100px; top: 296px; width: 550px; text-align: center; font-family: "Libre Baskerville", serif; font-weight: 700; text-transform: uppercase; white-space: nowrap; }
  .admission__plain { color: #e2e2e2; font-size: 19px; }
  .admission__accent { color: var(--red); font-size: 29px; }

  .perforation { position: absolute; left: 659px; top: 0; width: 0; height: 347px; border-left: 1px dashed #8c8c8c; }
  .stub-form { position: absolute; left: 660px; top: 0; width: 295px; height: 347px; }

  .form-field { position: absolute; left: 686px; right: 32px; height: 20px; display: flex; align-items: flex-end; font-family: "Roboto Condensed", sans-serif; font-size: 16px; line-height: 20px; color: var(--label); }
  .form-field__line { flex: 1; border-bottom: 1.5px solid #222; margin-left: 8px; margin-bottom: 3px; }
  .form-blank { position: absolute; left: 686px; right: 32px; border-bottom: 1.5px solid #222; }

  .agent-photo { position: absolute; left: 0; top: 0; width: 260px; height: 344px; }

  .challenge { position: absolute; left: 262px; width: 660px; text-align: center; font-family: "Libre Baskerville", serif; font-weight: 700; color: var(--white); }
  .challenge__head { top: 28px; font-size: 26px; letter-spacing: 1px; }
  .challenge__body { top: 70px; font-size: 23px; line-height: 38px; letter-spacing: 0.5px; }
  .challenge__close { top: 148px; font-size: 27px; letter-spacing: 1px; }

  .divider { position: absolute; left: 266px; width: 659px; top: 202px; border-top: 2px solid var(--rule); }

  .agency-contact { position: absolute; left: 262px; top: 222px; width: 660px; text-align: center; font-family: "Libre Baskerville", serif; font-weight: 700; font-style: normal; color: var(--white); font-size: 21px; line-height: 35px; letter-spacing: 0.5px; }
  .agency-contact__web { font-size: 19px; }
</style>
</head>
<body>
<main class="canvas">

  <section class="ticket ticket--front" aria-label="Admission ticket front">
    <div class="sports-backdrop" role="img" aria-label="Dark chalkboard background with faint sports equipment drawings"></div>
    <svg class="red-band" viewBox="0 0 110 347" preserveAspectRatio="none" aria-hidden="true">
      <polygon fill="var(--red)" points="0,0 80,0 76,14 84,30 78,48 86,66 80,88 90,110 84,130 94,150 88,172 96,196 92,218 100,240 94,262 102,286 98,306 106,328 104,347 0,347"/>
    </svg>

    <div class="school-mark school-mark--main"><span class="school-mark__box"></span>BRENWICK</div>
    <div class="serial serial--main">SR. NO.</div>

    <h1 class="school-name">
      <span class="school-name__line">BRENWICK</span>
      <span class="school-name__line">HIGH SCHOOL</span>
    </h1>

    <p class="admission">
      <span class="admission__plain">Admission</span>
      <span class="admission__accent">Opne</span>
      <span class="admission__plain">for</span>
      <span class="admission__accent">All Sports</span>
    </p>

    <div class="perforation"></div>
    <div class="school-mark school-mark--stub"><span class="school-mark__box"></span>BRENWICK</div>
    <div class="serial serial--stub">SR. NO.</div>

    <svg class="stub-form" viewBox="0 0 295 347" preserveAspectRatio="none" aria-hidden="true">
      <polygon fill="var(--white)" points="0,138 20,132 40,136 62,126 86,130 108,122 132,128 156,118 180,126 204,120 228,128 252,122 276,130 295,124 295,347 0,347"/>
    </svg>

    <div class="form-field" style="top:157px">Name :<span class="form-field__line"></span></div>
    <div class="form-blank" style="top:200px"></div>
    <div class="form-field" style="top:213px">Address :<span class="form-field__line"></span></div>
    <div class="form-blank" style="top:257px"></div>
    <div class="form-field" style="top:264px">Phone :<span class="form-field__line"></span></div>
    <div class="form-field" style="top:290px">Email :<span class="form-field__line"></span></div>
  </section>

  <section class="ticket ticket--back" aria-label="Sponsor advertisement on ticket back">
    <svg class="agent-photo" viewBox="0 0 260 344" preserveAspectRatio="none" role="img" aria-label="Portrait photo of agent Doran Pike in a dark suit">
      <defs>
        <linearGradient id="photoTone" x1="0" y1="0" x2="0.6" y2="1">
          <stop offset="0" stop-color="var(--photo-warm)"/>
          <stop offset="1" stop-color="var(--photo-cool)"/>
        </linearGradient>
      </defs>
      <polygon fill="url(#photoTone)" points="0,0 246,0 240,20 248,42 242,64 250,88 244,112 252,136 246,160 254,184 248,208 256,232 250,256 258,280 252,304 260,326 256,344 0,344"/>
      <polyline fill="none" stroke="var(--white)" stroke-width="2" points="246,0 240,20 248,42 242,64 250,88 244,112 252,136 246,160 254,184 248,208 256,232 250,256 258,280 252,304 260,326 256,344"/>
    </svg>

    <h2 class="challenge challenge__head">TAKE THE DORAN PIKE CHALLENGE:</h2>
    <p class="challenge challenge__body">If I can't save you money on<br>your Auto Insurance;</p>
    <p class="challenge challenge__close">I'LL BUY YOU DINNER!</p>

    <div class="divider"></div>

    <address class="agency-contact">
      482 N Alder Street Brenwick, OK 74990<br>
      Office : 555 214 7100 Fax : 555 214 7190<br>
      <span class="agency-contact__web">www.harvestlineagent.example/dpike</span>
    </address>
  </section>

</main>
</body>
</html>
```